Wordpress Design Project For Budget Hotel

Although it is a budget hotel we would like a mid to upmarket word press web design with relatively prominent images of local attractions. The design needs to be clean and professional looking.

This is design only. The design/files most be easy for our developer to work with and develop the back end/code.

The website will contain 6 pages:
Homepage
Accommodation & Rates
Facilities
Attractions
Bookings
Contact us

The full content is provided in a word doc which i have uploaded along with all the images needed.

Target Market(s)

The target audience are budget travelers looking for clean and comfortable accommodation at an affordable price.

Industry/Entity Type

Hotel

Requirements
Must have
• Prominent images of local attractions in a changing background or as a sliding banner.

Bookwise Hotel Reservation booking form. A small one on the home page and full one on the booking page.

Google maps window in the contact page
Should not have
• We dont want to many bright colours (ie yellow, red) but clean white is fine

```html
<!DOCTYPE html>
<html lang="en">
<head>
<meta charset="utf-8">
<title>Ridgeview Hotel Ashford – Facilities</title>
<link href="https://fonts.googleapis.com/css2?family=Questrial&family=Varela+Round&family=Crimson+Text&display=swap" rel="stylesheet">
<style>
:root{
  --green:#6a9a2a;
  --green-dark:#0f7a3e;
  --green-text:#1a7a3a;
  --text:#222;
  --muted:#555;
  --footer-bg:#ececec;
  --field:#a9a9a9;
  --white:#fff;
}
*{box-sizing:border-box;margin:0;padding:0}
html,body{width:941px;height:1200px;overflow:hidden;background:var(--white);font-family:Arial,Helvetica,sans-serif;color:var(--text)}
.page{position:relative;width:941px;height:1200px}
.brand{position:absolute;left:15px;top:36px;display:flex;align-items:center;gap:8px;font-family:'Questrial',sans-serif;font-size:25px;color:var(--green-text)}
.brand-mark{width:14px;height:14px;background:var(--green)}
.contact-top{position:absolute;right:19px;top:8px;text-align:right;font-family:'Questrial',sans-serif;color:var(--green)}
.contact-top .label{font-size:18px;letter-spacing:.3px}
.contact-top .phone{font-size:24px;display:flex;align-items:center;justify-content:flex-end;gap:6px;line-height:1.05}
.contact-top .mail{font-family:Arial,sans-serif;font-size:10px;color:var(--green-dark);margin-top:3px}
.main-nav{position:absolute;left:0;top:75px;width:941px;height:36px;background:var(--green);display:flex}
.main-nav a{display:flex;align-items:center;justify-content:center;color:var(--white);font-size:14px;text-decoration:none;height:100%}
.main-nav a.current{background:var(--green-dark)}
.hero{position:absolute;left:0;top:111px;width:941px;height:223px;background:linear-gradient(100deg,#8a7a74 0%,#b3202a 25%,#5e4a48 45%,#2b2626 70%,#a8a2a0 100%)}
.section-tag{position:absolute;left:15px;top:359px;width:132px;height:48px;background:var(--green);border-radius:4px;color:var(--white);font-family:'Questrial',sans-serif;font-size:24px;display:flex;align-items:center;justify-content:center}
.section-tag-arrow{position:absolute;left:146px;top:359px}
.content{position:absolute;left:17px;top:425px;width:590px;font-size:14px;line-height:17px}
.content h2{font-family:Arial,sans-serif;font-weight:normal;font-size:23px;margin-bottom:2px;line-height:28px}
.content p{margin-bottom:15px}
.content .block{margin-bottom:18px}
.gallery{position:absolute;left:13px;top:645px;width:595px;height:297px;border:1px solid #ddd;display:grid;grid-template-columns:repeat(3,193px);grid-template-rows:repeat(2,144px);gap:5px;padding:2px}
.gallery div{width:193px;height:144px}
.g1{background:linear-gradient(#c8413a,#4f6a3a 70%,#2f9a3a)}
.g2{background:linear-gradient(135deg,#c9c4b7,#b3202a 45%,#333)}
.g3{background:linear-gradient(#bfae90,#5b4a3e 70%,#3a3631)}
.g4{background:linear-gradient(#b86b4c,#9b8a78 60%,#c9b9a0)}
.g5{background:linear-gradient(#b8cde0,#7d8f8a 40%,#2f4a2a)}
.g6{background:linear-gradient(135deg,#b98a4a,#c9c7b8 45%,#2c6a3a)}
.booking-title{position:absolute;left:650px;top:360px;font-family:'Questrial',sans-serif;font-size:25px;color:var(--green-dark)}
.booking{position:absolute;left:650px;top:401px;width:268px;height:224px;border:1px solid #ccc;border-radius:4px;background:#f4f4f4;font-family:'Crimson Text',serif;font-size:12px;padding:14px 14px}
.booking label{display:block;line-height:12px}
.date-row{display:flex;align-items:center;gap:5px;margin-bottom:10px}
.date-row .field{width:82px;height:18px;border:1px solid #ccc;background:var(--white);font-size:13px;padding-left:2px;line-height:17px}
.nights{color:var(--muted);font-size:11px;margin-top:-4px}
.persons{border-top:1px solid #ddd;border-bottom:1px solid #ddd;margin:10px -4px 0;padding:6px 4px;display:flex;align-items:center;gap:5px;font-size:14px}
.select{width:38px;height:16px;border:1px solid #aaa;background:var(--white);font-size:10px;display:flex;justify-content:space-between;align-items:center;padding-left:3px}
.select span{width:13px;height:12px;border:1px solid #666;font-size:7px;text-align:center;line-height:11px}
.search-btn{margin-top:20px;width:78px;height:24px;border:1px solid #888;border-radius:2px;background:linear-gradient(#fafafa,#ddd);font-family:'Crimson Text',serif;font-size:15px;display:flex;align-items:center;justify-content:center}
.powered{position:absolute;right:14px;bottom:16px;font-size:8px;color:#888}
.site-footer{position:absolute;left:0;top:986px;width:941px;height:214px;background:var(--footer-bg)}
.site-footer h3{font-family:'Varela Round',sans-serif;font-size:18px;color:var(--green);font-weight:normal;position:absolute;top:27px}
.foot-nav{position:absolute;left:31px;top:62px;display:grid;grid-template-columns:147px 100px;font-size:12px;line-height:14px;color:#333}
.foot-form{position:absolute;left:346px;top:56px;width:184px}
.foot-form .input{background:var(--field);border-radius:3px;height:22px;color:var(--white);font-size:12px;font-weight:bold;padding:4px 10px;margin-bottom:3px}
.foot-form .input.message{height:51px}
.foot-form .submit{margin-top:5px;width:60px;height:21px;background:var(--green);border-radius:3px;color:var(--white);font-size:12px;display:flex;align-items:center;justify-content:center}
.foot-contact{position:absolute;left:666px;top:57px;font-size:14px;color:#333}
.foot-contact .line{display:flex;align-items:center;gap:5px;font-size:12px;margin-top:6px}
</style>
</head>
<body>
<div class="page">
  <header>
    <div class="brand"><span class="brand-mark"></span>Ridgeview Hotel Ashford</div>
    <div class="contact-top">
      <div class="label">CONTACT US NOW</div>
      <div class="phone">
        <svg width="16" height="18" viewBox="0 0 16 18"><path d="M4 1 L7 5 L5 7 Q7 11 10 13 L12 11 L15 14 L12 17 Q4 14 1 4 Z" fill="none" stroke="currentColor" stroke-width="1.6"/></svg>
        02 6555 0148
      </div>
      <div class="mail">stay@ridgeviewhotel.example</div>
    </div>
  </header>

  <nav class="main-nav">
    <a style="width:97px">Home</a>
    <a style="width:128px">About Us</a>
    <a style="width:206px">Accomodation &amp; Rates</a>
    <a class="current" style="width:107px">Facilities</a>
    <a style="width:134px">Attractions</a>
    <a style="width:129px">Bookings</a>
    <a style="width:140px">Contact Us</a>
  </nav>

  <div class="hero" role="img" aria-label="Hotel lounge with red sofa and white coffee table"></div>

  <div class="section-tag">Facilities</div>
  <svg class="section-tag-arrow" width="25" height="48" viewBox="0 0 25 48"><path d="M0 0 L24 24 L0 48 Z" fill="var(--green-dark)"/></svg>

  <main class="content">
    <section class="block">
      <h2>Food</h2>
      <p>We have an extensive Chinese menu, with great $7 lunchtime specials (eat in or takeaway) Australian meals are also available, including chargrilled steaks from $18.</p>
    </section>
    <section class="block">
      <h2>Bar</h2>
      <p>One of the last great horseshoe bars with pool table and big screen TV for sports. Wagering &amp; lotto are available. We also have a covered breakout area with uncovered seating for the sun lovers.</p>
      <p>Our verandah dining area has views over a picturesque landscape.</p>
    </section>
  </main>

  <div class="gallery">
    <div class="g1" role="img" aria-label="Horseshoe bar with pool table"></div>
    <div class="g2" role="img" aria-label="Lounge area with red sofa"></div>
    <div class="g3" role="img" aria-label="Dining room with lounge seating"></div>
    <div class="g4" role="img" aria-label="Courtyard with picnic table"></div>
    <div class="g5" role="img" aria-label="View over green hills"></div>
    <div class="g6" role="img" aria-label="Wine glasses by the fireplace"></div>
  </div>

  <h2 class="booking-title">Quick Booking</h2>
  <aside class="booking">
    <label>Check-in:</label>
    <div class="date-row"><div class="field">09/01/2013</div>
      <svg width="16" height="17" viewBox="0 0 16 17"><rect x="0.5" y="0.5" width="15" height="16" fill="#fff" stroke="#5a7fb0"/><rect x="0.5" y="0.5" width="15" height="4" fill="#5a7fb0"/><path d="M3 7h10M3 10h10M3 13h10M6 5v11M10 5v11" stroke="#8aa5cc"/></svg></div>
    <label>Check-out:</label>
    <div class="date-row"><div class="field">09/02/2013</div>
      <svg width="16" height="17" viewBox="0 0 16 17"><rect x="0.5" y="0.5" width="15" height="16" fill="#fff" stroke="#5a7fb0"/><rect x="0.5" y="0.5" width="15" height="4" fill="#5a7fb0"/><path d="M3 7h10M3 10h10M3 13h10M6 5v11M10 5v11" stroke="#8aa5cc"/></svg></div>
    <div class="nights">Nights: 1</div>
    <div class="persons">Number of persons: <div class="select">1<span>▼</span></div></div>
    <div class="search-btn">Search »</div>
    <div class="powered">Powered by Bookwise</div>
  </aside>

  <footer class="site-footer">
    <h3 style="left:31px">navigation</h3>
    <div class="foot-nav">
      <span>Home</span><span>About Us</span>
      <span>Accomodation &amp; Rates</span><span>Sitemap</span>
      <span>Facilities</span><span>Bookings</span>
      <span>Attractions</span><span>Contact Us</span>
    </div>
    <h3 style="left:350px">email us</h3>
    <div class="foot-form">
      <div class="input">name</div>
      <div class="input">email</div>
      <div class="input message">message</div>
      <div class="submit">submit</div>
    </div>
    <h3 style="left:666px">contact us</h3>
    <div class="foot-contact">
      <div>14-18 Wattle St, ASHFORD, NSW 2361</div>
      <div class="line"><svg width="13" height="13" viewBox="0 0 13 13"><circle cx="6.5" cy="6.5" r="6" fill="none" stroke="#333"/><path d="M4 3l1.5 2-1 1q1 2 2.5 2.5l1-1 2 1.5-1.5 1.5Q5 10 3 4.5Z" fill="#333"/></svg>02 6555 0148</div>
      <div class="line"><svg width="13" height="11" viewBox="0 0 13 11"><path d="M1 4 L6.5 1 L12 4 V10 H1 Z M1 4 L6.5 7.5 L12 4" fill="none" stroke="#333"/></svg>stay@ridgeviewhotel.example</div>
    </div>
  </footer>
</div>
</body>
</html>
```